依頼詳細
既に新規顧客向けのチラシを作成しており、それがベースになります。
必要なデータや参考となる資料を添付しています。

修正内容の大まかな原案を作成しておりますが、最低限必要な事項を記載しているだけですので大幅にデザイン変更して頂いて構いません。 見やすく目的に沿った内容であれば、画像等の追加、文章やフレーズ、フォント、文字サイズなどの修正、加筆もOKです。基本的にはデザインを重視したいと思います。

印刷はA4サイズ両面(297x210mm)です。
表面はフルカラーで【商品案内】、裏面は白黒で【FAX専用注文書】となります。

商品に相応しい爽やかな印象を持っていただけるデザインを希望しますが、一目でお得感が分かりリピートしたくなるような工夫をお願いいたします。
記載項目

```html
<!DOCTYPE html>
<html lang="ja">
<head>
<meta charset="utf-8">
<title>リピート専用ご注文シート</title>
<link href="https://fonts.googleapis.com/css2?family=Noto+Sans+JP:wght@400;500;700;900&display=swap" rel="stylesheet">
<style>
:root{
  --ink:#161616;
  --line:#3a3a3a;
  --soft:#d8d8d8;
  --pale:#efefef;
  --paper:#ffffff;
  --mid:#7a7a7a;
}
*{box-sizing:border-box;margin:0;padding:0}
html,body{width:849px;height:1200px;overflow:hidden;background:var(--paper)}
body{font-family:"Noto Sans JP",sans-serif;color:var(--ink);font-size:10px;line-height:1.25}
.sheet{position:relative;width:849px;height:1200px;padding:10px 14px 0}

/* header */
.masthead{display:flex;align-items:stretch;height:50px;gap:8px}
.fax-direction{width:62px;border:2px solid var(--ink);display:flex;flex-direction:column;align-items:center;justify-content:center;font-weight:700;font-size:10px;line-height:1.1}
.fax-direction svg{margin-top:2px}
.title-band{flex:1;background:var(--ink);color:var(--paper);display:flex;align-items:center;justify-content:center;font-size:27px;font-weight:900;letter-spacing:3px}
.masthead-aside{width:220px;display:flex;flex-direction:column;justify-content:space-between;font-size:9px}
.order-date{border:1.5px solid var(--ink);height:28px;display:flex;align-items:center;padding:0 8px;gap:14px;font-size:11px;font-weight:700}
.order-date span.gap{flex:1}

/* sections */
.section{margin-top:7px}
.section-head{display:flex;align-items:center;gap:10px;border-bottom:2px solid var(--ink);height:22px}
.section-label{background:var(--ink);color:var(--paper);font-weight:700;font-size:13px;padding:2px 12px;height:22px;display:flex;align-items:center}
.section-note{font-size:9px;color:var(--ink)}
.form-grid{display:grid;border-left:1px solid var(--line);border-top:0}
.cell{border-right:1px solid var(--line);border-bottom:1px solid var(--line);padding:3px 6px;display:flex;align-items:center;font-size:10px}
.cell.label{background:var(--pale);font-weight:700;font-size:11px;justify-content:center}
.cell.small{font-size:8.5px;align-items:flex-start}
.orderer{grid-template-columns:70px 1fr 80px 220px}
.delivery{grid-template-columns:70px 1fr 80px 220px}
.box{display:inline-block;width:11px;height:11px;border:1.3px solid var(--ink);margin-right:4px;vertical-align:-2px;background:var(--paper)}
.option{margin-right:16px;font-weight:500;white-space:nowrap}
.postal{font-weight:700;margin-right:10px}

.payment-row{display:flex;align-items:center;border:1px solid var(--line);border-top:0;height:30px;padding:0 10px;font-size:11px}
.payment-row .note{font-size:8.5px;margin-left:auto;color:var(--mid)}

.twin{display:flex;gap:10px;margin-top:7px}
.twin > .panel{flex:1}
.panel-body{border:1px solid var(--line);border-top:0}
.check-line{display:flex;align-items:center;height:24px;padding:0 8px;border-bottom:1px solid var(--line);font-size:10.5px}
.check-line:last-child{border-bottom:0}
.slip-grid{display:grid;grid-template-columns:62px 1fr 60px 1fr;}
.slip-grid .cell{height:36px}

/* products */
.products{display:grid;grid-template-columns:repeat(4,1fr);gap:6px;margin-top:8px}
.product{border:1.5px solid var(--ink)}
.product-head{background:var(--ink);color:var(--paper);display:flex;align-items:center;justify-content:space-between;padding:4px 6px;height:30px}
.product-name{font-size:14px;font-weight:900;letter-spacing:1px}
.product-code{background:var(--paper);color:var(--ink);font-size:9px;font-weight:700;padding:1px 4px}
.price-table{width:100%;border-collapse:collapse;table-layout:fixed}
.price-table th{background:var(--soft);font-size:8.5px;font-weight:700;height:20px;border:1px solid var(--line)}
.price-table td{border:1px solid var(--line);height:35px;text-align:center;font-size:10px}
.price-table td.set{font-weight:700;font-size:10.5px;line-height:1.15}
.price-table td.set small{display:block;font-size:7.5px;font-weight:500}
.price-table td.price{text-align:right;padding-right:5px;font-weight:700;font-size:11px}
.price-table td.qty{font-size:8px;text-align:right;padding-right:4px;vertical-align:bottom}
.price-table col.c1{width:26%}
.price-table col.c2{width:18%}
.price-table col.c3{width:32%}
.price-table col.c4{width:24%}

/* shipping + time */
.logistics{display:flex;gap:10px;margin-top:8px}
.shipping{flex:1.25}
.ship-table{width:100%;border-collapse:collapse;font-size:9px}
.ship-table th,.ship-table td{border:1px solid var(--line);height:19px;text-align:center}
.ship-table th{background:var(--soft);font-weight:700}
.delivery-time{flex:1}
.time-grid{display:grid;grid-template-columns:60px 1fr 1fr;border-left:1px solid var(--line)}
.time-grid .cell{height:26px;font-size:10.5px}

/* totals */
.totals{display:grid;grid-template-columns:repeat(4,1fr);border-left:1.5px solid var(--ink);border-top:1.5px solid var(--ink);margin-top:8px}
.total-cell{border-right:1.5px solid var(--ink);border-bottom:1.5px solid var(--ink);height:50px;padding:3px 6px;display:flex;flex-direction:column;justify-content:space-between}
.total-cell .t-label{font-size:9.5px;font-weight:700}
.total-cell .t-unit{text-align:right;font-size:12px;font-weight:700}
.total-cell.grand{background:var(--pale)}

.remarks{margin-top:7px;border:1px solid var(--line);height:48px;padding:4px 8px;font-size:9px}
.remarks b{font-size:10.5px}

/* footer */
.footer{position:absolute;left:0;right:0;bottom:0;height:44px;background:var(--ink);color:var(--paper);display:flex;align-items:center;padding:0 18px;gap:14px}
.footer-hours{font-size:19px;font-weight:900}
.footer-fax{background:var(--paper);color:var(--ink);font-weight:900;font-size:16px;padding:0 6px}
.footer-number{font-size:32px;font-weight:900;letter-spacing:1px}
.footer-company{margin-left:auto;font-size:17px;font-weight:700;display:flex;align-items:center;gap:7px}
.footer-company i{display:inline-block;width:12px;height:12px;background:var(--paper)}
</style>
</head>
<body>
<div class="sheet">

  <header class="masthead">
    <div class="fax-direction">FAX<br>送信方向
      <svg width="18" height="12" viewBox="0 0 18 12"><path d="M9 0 L18 12 H0 Z" fill="#161616"/></svg>
    </div>
    <h1 class="title-band">リピート専用ご注文シート</h1>
    <div class="masthead-aside">
      <div>本紙はお手数ですがコピーしてご使用ください</div>
      <div class="order-date">ご注文日<span class="gap"></span>年<span>　</span>月<span>　</span>日</div>
    </div>
  </header>

  <section class="section">
    <div class="section-head"><div class="section-label">ご注文者情報</div><div class="section-note">※太枠は必ずご記入ください。ご住所・お名前は配送先の確認に使用します。</div></div>
    <div class="form-grid orderer">
      <div class="cell label" style="grid-row:span 2;height:60px">お名前</div>
      <div class="cell small" style="grid-row:span 2">フリガナ</div>
      <div class="cell label" style="height:30px">電話番号</div>
      <div class="cell"></div>
      <div class="cell label" style="height:30px">FAX番号</div>
      <div class="cell"></div>
      <div class="cell label" style="height:50px">ご住所</div>
      <div class="cell small" style="grid-column:span 3"><span class="postal">〒　　　－</span></div>
      <div class="cell label" style="height:30px">Eメール</div>
      <div class="cell" style="grid-column:span 3"></div>
    </div>
  </section>

  <section class="section">
    <div class="section-head"><div class="section-label">お届け先情報</div><div class="section-note">※ご注文者様と異なる場合のみご記入ください。</div></div>
    <div class="form-grid delivery">
      <div class="cell label" style="height:40px">お名前</div>
      <div class="cell small">フリガナ</div>
      <div class="cell label">電話番号</div>
      <div class="cell"></div>
      <div class="cell label" style="height:44px">ご住所</div>
      <div class="cell small" style="grid-column:span 3"><span class="postal">〒　　　－</span></div>
    </div>
  </section>

  <section class="section">
    <div class="section-head"><div class="section-label">お支払い方法</div><div class="section-note">※ご希望の方法に印をつけてください。</div></div>
    <div class="payment-row">
      <span class="option"><span class="box"></span>代金引換</span>
      <span class="option"><span class="box"></span>銀行振込（前払い）</span>
      <span class="option"><span class="box"></span>請求書払い（後払い）</span>
      <span class="note">※後払いは審査がございます。</span>
    </div>
  </section>

  <div class="twin">
    <section class="panel">
      <div class="section-head"><div class="section-label">ご請求書</div><div class="section-note">※必要な方は印をつけてください。</div></div>
      <div class="panel-body">
        <div class="check-line"><span class="box"></span>商品に同封</div>
        <div class="check-line"><span class="box"></span>ご注文者様のご住所へ郵送</div>
        <div class="check-line"><span class="box"></span>お届け先のご住所へ郵送</div>
      </div>
    </section>
    <section class="panel">
      <div class="section-head"><div class="section-label">伝票発行</div><div class="section-note">※ご希望の内容に印をつけてください。</div></div>
      <div class="panel-body slip-grid">
        <div class="cell label">納品書</div><div class="cell"><span class="box"></span>要　<span class="box" style="margin-left:10px"></span>不要</div>
        <div class="cell label">金額</div><div class="cell"><span class="box"></span>表記　<span class="box"></span>非表記</div>
        <div class="cell label">領収書</div><div class="cell"><span class="box"></span>要　<span class="box" style="margin-left:10px"></span>不要</div>
        <div class="cell label">宛名</div><div class="cell"></div>
      </div>
    </section>
  </div>

  <section class="products">
    <article class="product">
      <div class="product-head"><span class="product-name">工業用精製水</span><span class="product-code">TSP-01</span></div>
      <table class="price-table">
        <colgroup><col class="c1"><col class="c2"><col class="c3"><col class="c4"></colgroup>
        <tr><th>セット</th><th>コック</th><th>金額(税込)</th><th>数量</th></tr>
        <tr><td class="set" rowspan="2">単品</td><td>なし</td><td class="price">¥ 825</td><td class="qty">箱</td></tr>
        <tr><td>あり</td><td class="price">¥ 948</td><td class="qty">箱</td></tr>
        <tr><td class="set" rowspan="2">5箱<small>まとめ買い</small></td><td>なし</td><td class="price">¥4,402</td><td class="qty">組</td></tr>
        <tr><td>あり</td><td class="price">¥5,000</td><td class="qty">組</td></tr>
        <tr><td class="set" rowspan="2">10箱<small>まとめ買い</small></td><td>なし</td><td class="price">¥8,585</td><td class="qty">組</td></tr>
        <tr><td>あり</td><td class="price">¥8,970</td><td class="qty">組</td></tr>
        <tr><td class="set" rowspan="2">20箱<small>まとめ買い</small></td><td>なし</td><td class="price">¥16,555</td><td class="qty">組</td></tr>
        <tr><td>あり</td><td class="price">¥17,745</td><td class="qty">組</td></tr>
      </table>
    </article>
    <article class="product">
      <div class="product-head"><span class="product-name">バッテリー補充液</span><span class="product-code">TSP-02</span></div>
      <table class="price-table">
        <colgroup><col class="c1"><col class="c2"><col class="c3"><col class="c4"></colgroup>
        <tr><th>セット</th><th>コック</th><th>金額(税込)</th><th>数量</th></tr>
        <tr><td class="set" rowspan="2">単品</td><td>なし</td><td class="price">¥ 825</td><td class="qty">箱</td></tr>
        <tr><td>あり</td><td class="price">¥ 948</td><td class="qty">箱</td></tr>
        <tr><td class="set" rowspan="2">5箱<small>まとめ買い</small></td><td>なし</td><td class="price">¥4,402</td><td class="qty">組</td></tr>
        <tr><td>あり</td><td class="price">¥4,990</td><td class="qty">組</td></tr>
        <tr><td class="set" rowspan="2">10箱<small>まとめ買い</small></td><td>なし</td><td class="price">¥8,585</td><td class="qty">組</td></tr>
        <tr><td>あり</td><td class="price">¥9,360</td><td class="qty">組</td></tr>
        <tr><td class="set" rowspan="2">20箱<small>まとめ買い</small></td><td>なし</td><td class="price">¥16,965</td><td class="qty">組</td></tr>
        <tr><td>あり</td><td class="price">¥17,745</td><td class="qty">組</td></tr>
      </table>
    </article>
    <article class="product">
      <div class="product-head"><span class="product-name">高純度精製水</span><span class="product-code">TSP-03</span></div>
      <table class="price-table">
        <colgroup><col class="c1"><col class="c2"><col class="c3"><col class="c4"></colgroup>
        <tr><th>セット</th><th>コック</th><th>金額(税込)</th><th>数量</th></tr>
        <tr><td class="set" rowspan="2">単品</td><td>なし</td><td class="price">¥1,155</td><td class="qty">箱</td></tr>
        <tr><td>あり</td><td class="price">¥1,287</td><td class="qty">箱</td></tr>
        <tr><td class="set" rowspan="2">5箱<small>まとめ買い</small></td><td>なし</td><td class="price">¥5,092</td><td class="qty">組</td></tr>
        <tr><td>あり</td><td class="price">¥5,940</td><td class="qty">組</td></tr>
        <tr><td class="set" rowspan="2">10箱<small>まとめ買い</small></td><td>なし</td><td class="price">¥10,517</td><td class="qty">組</td></tr>
        <tr><td>あり</td><td class="price">¥11,044</td><td class="qty">組</td></tr>
        <tr><td class="set" rowspan="2">20箱<small>まとめ買い</small></td><td>なし</td><td class="price">¥19,910</td><td class="qty">組</td></tr>
        <tr><td>あり</td><td class="price">¥20,592</td><td class="qty">組</td></tr>
      </table>
    </article>
    <article class="product">
      <div class="product-head"><span class="product-name">高純度精製水</span><span class="product-code">TSP-04</span></div>
      <table class="price-table">
        <colgroup><col class="c1"><col class="c2"><col class="c3"><col class="c4"></colgroup>
        <tr><th>セット</th><th>コック</th><th>金額(税込)</th><th>数量</th></tr>
        <tr><td class="set" rowspan="2">単品</td><td>なし</td><td class="price">¥1,155</td><td class="qty">箱</td></tr>
        <tr><td>あり</td><td class="price">¥1,287</td><td class="qty">箱</td></tr>
        <tr><td class="set" rowspan="2">5箱<small>まとめ買い</small></td><td>なし</td><td class="price">¥5,082</td><td class="qty">組</td></tr>
        <tr><td>あり</td><td class="price">¥6,290</td><td class="qty">組</td></tr>
        <tr><td class="set" rowspan="2">10箱<small>まとめ買い</small></td><td>なし</td><td class="price">¥10,164</td><td class="qty">組</td></tr>
        <tr><td>あり</td><td class="price">¥11,440</td><td class="qty">組</td></tr>
        <tr><td class="set" rowspan="2">20箱<small>まとめ買い</small></td><td>なし</td><td class="price">¥19,250</td><td class="qty">組</td></tr>
        <tr><td>あり</td><td class="price">¥21,780</td><td class="qty">組</td></tr>
      </table>
    </article>
  </section>

  <div class="logistics">
    <section class="shipping">
      <div class="section-head"><div class="section-label">送料及び代引手数料について</div></div>
      <table class="ship-table">
        <tr><th>地域</th><th>北海道</th><th>東北</th><th>関東・中部</th><th>近畿・中国</th><th>九州</th><th>沖縄</th></tr>
        <tr><th>送料</th><td>¥1,540</td><td>¥990</td><td>¥880</td><td>¥880</td><td>¥990</td><td>¥2,200</td></tr>
        <tr><th>代引</th><td colspan="6">1万円未満 ¥330／3万円未満 ¥440／3万円以上 ¥660</td></tr>
        <tr><td colspan="7" style="font-size:8.5px">※10箱以上のまとめ買いは送料無料となります。</td></tr>
      </table>
    </section>
    <section class="delivery-time">
      <div class="section-head"><div class="section-label">お届け日時指定</div></div>
      <div class="time-grid">
        <div class="cell label" style="grid-row:span 3">時間帯</div>
        <div class="cell"><span class="box"></span>午前中</div><div class="cell"><span class="box"></span>16〜18時</div>
        <div class="cell"><span class="box"></span>12〜14時</div><div class="cell"><span class="box"></span>18〜20時</div>
        <div class="cell"><span class="box"></span>14〜16時</div><div class="cell"><span class="box"></span>20〜21時</div>
      </div>
    </section>
  </div>

  <section class="totals">
    <div class="total-cell"><span class="t-label">商品代金合計（税込）</span><span class="t-unit">円</span></div>
    <div class="total-cell"><span class="t-label">送料（税込）</span><span class="t-unit">円</span></div>
    <div class="total-cell"><span class="t-label">代引手数料（税込）</span><span class="t-unit">円</span></div>
    <div class="total-cell grand"><span class="t-label">ご請求金額（合計）</span><span class="t-unit">円</span></div>
  </section>

  <section class="remarks"><b>ご連絡事項</b>　ご要望などございましたらご記入ください。</section>

  <footer class="footer">
    <span class="footer-hours">24時間受付</span>
    <span class="footer-fax">FAX</span>
    <span class="footer-number">0120-555-218</span>
    <span class="footer-company"><i></i>ミナモ化学株式会社</span>
  </footer>
</div>
</body>
</html>
```